flyer for letter box drop 2012

Advertising flyer that is delivered to homes in our suburb.
We are optometrists and looking to have a flyer delivered into our local area residential letterboxes. As a business that has been in the area for 25 years we are looking for an innovative approach to keeping our existing customers as well as appealing to the new generation.
We would like the flyer to reflect or professional eye care services
and commitment to quality service and products.
We do not promote our selves as a discount outlet for eg 2 for 1,50% of everything.
I have attached a copy of the flyer we have been using for the last 12 months.

Target Market(s)

25- 70 year olds male and female

Industry/Entity Type

Residential

Requirements
Must have
• flyer should be double sided a5 page
Prominent logo display
address ,phone number , web address,

```html
<!DOCTYPE html>
<html lang="en">
<head>
<meta charset="utf-8">
<title>Halden Lane Optical – Flyer</title>
<link rel="stylesheet" href="https://fonts.googleapis.com/css2?family=Arimo:wght@400;700&family=Roboto+Condensed:wght@300;400&display=swap">
<style>
  :root {
    --green: #2fa845;
    --blue: #2a5fa8;
    --ink: #3a3a3a;
    --soft-ink: #555555;
    --rule: #8a8a8a;
    --amp: #ececec;
    --paper: #ffffff;
  }
  * { margin: 0; padding: 0; box-sizing: border-box; }
  html, body { width: 855px; height: 1200px; overflow: hidden; background: var(--paper); }
  .flyer {
    position: relative;
    width: 855px;
    height: 1200px;
    overflow: hidden;
    background: var(--paper);
    font-family: "Arimo", Arial, sans-serif;
    color: var(--ink);
  }
  .top-band {
    position: absolute; left: 0; top: 108px;
    width: 570px; height: 46px;
    background: var(--green);
    color: #fff;
    font-size: 19px;
    line-height: 46px;
    padding-left: 62px;
  }
  .top-block {
    position: absolute; right: 0; top: 108px;
    width: 52px; height: 46px;
    background: var(--green);
  }
  .brand {
    position: absolute; left: 596px; top: 92px;
    width: 190px;
    text-align: center;
    color: var(--blue);
    font-weight: 400;
  }
  .brand-line-1 { display: block; font-size: 25px; line-height: 30px; }
  .brand-line-2 { display: block; font-size: 44px; line-height: 48px; }
  .hero-photo {
    position: absolute; left: 0; top: 190px;
    width: 560px; height: 640px;
  }
  .amp {
    position: absolute; left: 470px; top: 360px;
    font-family: "Roboto Condensed", Arial, sans-serif;
    font-weight: 300;
    font-size: 250px;
    line-height: 1;
    color: var(--amp);
  }
  .headline {
    position: absolute;
    font-family: "Roboto Condensed", Arial, sans-serif;
    font-weight: 300;
    color: var(--ink);
    text-align: right;
    line-height: 1;
    white-space: nowrap;
  }
  .headline.small { font-size: 54px; }
  .headline.large { font-size: 88px; }
  .h-latest { right: 178px; top: 270px; }
  .h-spectacle { right: 90px; top: 314px; }
  .h-contact { right: 128px; top: 450px; }
  .h-lenses { right: 114px; top: 492px; }
  .features {
    position: absolute; left: 506px; top: 718px;
    list-style: none;
    font-size: 19px;
    line-height: 23px;
    color: var(--ink);
  }
  .features li { position: relative; padding-left: 14px; }
  .features li::before {
    content: ""; position: absolute; left: 0; top: 8px;
    width: 7px; height: 7px; border-radius: 50%;
    background: var(--green);
  }
  .rule { position: absolute; height: 2px; background: var(--rule); }
  .rule-mid { left: 0; top: 864px; width: 622px; }
  .rule-foot { left: 224px; top: 1106px; width: 631px; }
  .exams {
    position: absolute; left: 0; top: 922px; width: 855px;
    text-align: center;
  }
  .exams-title { font-size: 28px; color: var(--soft-ink); margin-bottom: 12px; }
  .exams-list { font-size: 17px; line-height: 25px; color: var(--soft-ink); }
  .contact {
    position: absolute; left: 0; top: 1122px; width: 912px;
    text-align: center;
    font-size: 17px;
    letter-spacing: 5px;
    line-height: 30px;
    color: var(--soft-ink);
  }
  .contact .web-accent { color: var(--green); font-weight: 700; }
</style>
</head>
<body>
<div class="flyer">
  <div class="top-band">Independent Optometrists Servicing Brookvale since 1989</div>
  <div class="brand" aria-label="Halden Lane Optical">
    <span class="brand-line-1">Halden Lane</span>
    <span class="brand-line-2">Optical</span>
  </div>
  <div class="top-block"></div>

  <svg class="hero-photo" role="img" aria-label="Photo of a smiling woman in sunglasses wearing a headscarf and wooden bangles" viewBox="0 0 560 640">
    <defs>
      <radialGradient id="heroTone" cx="0.45" cy="0.45" r="0.6">
        <stop offset="0" stop-color="#c99a7a"/>
        <stop offset="0.6" stop-color="#e6d2c2"/>
        <stop offset="1" stop-color="#ffffff"/>
      </radialGradient>
    </defs>
    <rect width="560" height="640" fill="url(#heroTone)"/>
  </svg>

  <div class="amp">&amp;</div>
  <div class="headline small h-latest">Latest</div>
  <div class="headline large h-spectacle">Spectacle</div>
  <div class="headline small h-contact">Contact</div>
  <div class="headline large h-lenses">Lenses</div>

  <ul class="features">
    <li>Qualified and experienced Optometrist<br>and Optical Technician in store</li>
    <li>Direct billing to private health funds<br>with ClaimPoint</li>
    <li>On site lens fittings to own frames</li>
  </ul>

  <div class="rule rule-mid"></div>

  <div class="exams">
    <p class="exams-title">StateCare Bulk Billed Eye Examinations</p>
    <p class="exams-list">Glaucoma Assessment II Diabetes Vision Assessment<br>Cataract Assessment II Macula Degeneration Assessment<br>Retinal Photography</p>
  </div>

  <div class="rule rule-foot"></div>

  <div class="contact">
    <p>14B HALDEN LANE, BROOKVALE II TEL: 9555 0142</p>
    <p>www.HALDEN<span class="web-accent">LANE</span>OPTICAL.com.au</p>
  </div>
</div>
</body>
</html>
```